Design a (20.4 x 10.14) Banner that says - Keep Hope Rising From Harvest Crown TV Family

We want a design (20.4 x 10.14) with the words 'Keep Hope Rising' as the main text and 'From Harvest Crown TV Family' underneath. For 'Harvest Crown TV', we'd like you to use the logo which can be found in the image attached.

The image attached is just an example but please let your creative juices flow!

Target Market(s)

Christian

Industry/Entity Type

Christian

Requirements
Must have
• Must have the words 'Keep Hope Rising' and 'From Harvest Crown TV Family'.

```html
<!DOCTYPE html>
<html lang="en">
<head>
<meta charset="utf-8">
<title>Keep Hope Rising — Harvest Crown TV Family Banner</title>
<link href="https://fonts.googleapis.com/css2?family=Kaushan+Script&family=Josefin+Sans:wght@700&family=Montserrat:wght@700;800&display=swap" rel="stylesheet">
<style>
  :root {
    --page: #ffffff;
    --ink-dark: #0d0d12;
    --photo-gray-light: #5a5a5e;
    --photo-gray-dark: #141416;
    --blue-deep: #0a1a6e;
    --blue-bright: #2a3cf0;
    --teal: #0e5c7a;
    --cyan: #48d8ee;
    --violet: #6a4fd8;
    --gold: #e8c21c;
    --label-bg: #f2f2f2;
    --label-ink: #1f1f2a;
    --brand-ink: #3a2fb0;
  }
  * { margin: 0; padding: 0; box-sizing: border-box; }
  html, body {
    width: 1200px; height: 1000px; overflow: hidden;
    background: var(--page);
  }
  .banner {
    position: absolute;
    left: 84px; top: 265px;
    width: 1028px; height: 508px;
    overflow: hidden;
    background: var(--ink-dark);
  }
  .banner__art { position: absolute; inset: 0; width: 100%; height: 100%; }

  .headline { position: absolute; inset: 0; }
  .headline__keep {
    position: absolute; left: 368px; top: 20px;
    font-family: "Kaushan Script", cursive;
    font-size: 118px; line-height: 1;
    color: var(--cyan);
    text-shadow: -4px 4px 0 var(--violet);
    transform: rotate(-6deg);
  }
  .headline__hope {
    position: absolute; left: 318px; top: 140px;
    font-family: "Josefin Sans", sans-serif;
    font-weight: 700; font-size: 210px; line-height: 1;
    letter-spacing: -4px;
    color: var(--violet);
  }
  .headline__hope-outline {
    position: absolute; left: 334px; top: 150px;
    font-family: "Josefin Sans", sans-serif;
    font-weight: 700; font-size: 210px; line-height: 1;
    letter-spacing: -4px;
    color: transparent;
    -webkit-text-stroke: 3px #ffffff;
  }
  .headline__rising {
    position: absolute; left: 360px; top: 290px;
    font-family: "Kaushan Script", cursive;
    font-size: 112px; line-height: 1;
    color: var(--gold);
    text-shadow: -4px 4px 0 var(--violet);
    transform: rotate(-6deg);
  }

  .signoff {
    position: absolute; left: 316px; top: 449px;
    width: 392px; height: 44px;
    display: flex; align-items: center; justify-content: center; gap: 14px;
    font-family: "Montserrat", sans-serif;
    font-weight: 700; font-size: 17px; letter-spacing: 1.5px;
    color: var(--label-ink);
    text-transform: uppercase;
  }
  .signoff__plate { position: absolute; inset: 0; width: 100%; height: 100%; z-index: 0; }
  .signoff span { position: relative; z-index: 1; }
  .signoff__brand {
    font-weight: 800; font-size: 19px; letter-spacing: 0;
    text-transform: none; color: var(--brand-ink);
  }
</style>
</head>
<body>
  <section class="banner" aria-label="Keep Hope Rising banner">
    <svg class="banner__art" viewBox="0 0 1028 508" preserveAspectRatio="none">
      <defs>
        <radialGradient id="hands-photo" cx="50%" cy="50%" r="60%">
          <stop offset="0" stop-color="var(--photo-gray-light)"/>
          <stop offset="1" stop-color="var(--photo-gray-dark)"/>
        </radialGradient>
        <linearGradient id="left-photo" x1="0" y1="0" x2="1" y2="1">
          <stop offset="0" stop-color="var(--blue-bright)"/>
          <stop offset="0.6" stop-color="var(--blue-deep)"/>
          <stop offset="1" stop-color="var(--teal)"/>
        </linearGradient>
        <linearGradient id="right-photo" x1="1" y1="0" x2="0" y2="1">
          <stop offset="0" stop-color="var(--blue-bright)"/>
          <stop offset="0.5" stop-color="var(--teal)"/>
          <stop offset="1" stop-color="var(--blue-deep)"/>
        </linearGradient>
      </defs>
      <rect class="photo-hands" width="1028" height="508" fill="url(#hands-photo)" role="img" aria-label="Photo area: many hands joined together in a circle, black and white"/>
      <polygon class="photo-left" points="0,0 240,0 60,254 330,508 0,508" fill="url(#left-photo)" opacity="0.92" role="img" aria-label="Photo area: people reaching into the circle, tinted blue"/>
      <polygon class="photo-right" points="1028,0 700,0 900,254 700,508 1028,508" fill="url(#right-photo)" opacity="0.92" role="img" aria-label="Photo area: people reaching into the circle, tinted blue"/>
      <line x1="62" y1="15" x2="330" y2="508" stroke="var(--cyan)" stroke-width="3" opacity="0.85"/>
      <line x1="716" y1="0" x2="960" y2="508" stroke="var(--cyan)" stroke-width="3" opacity="0.85"/>
      <line x1="290" y1="10" x2="130" y2="330" stroke="var(--blue-bright)" stroke-width="2" opacity="0.8"/>
    </svg>

    <h1 class="headline" aria-label="Keep Hope Rising">
      <span class="headline__keep">Keep</span>
      <span class="headline__hope-outline" aria-hidden="true">HOPE</span>
      <span class="headline__hope">HOPE</span>
      <span class="headline__rising">Rising</span>
    </h1>

    <p class="signoff">
      <svg class="signoff__plate" viewBox="0 0 392 44" preserveAspectRatio="none" aria-hidden="true">
        <polygon points="0,0 392,0 378,44 14,44" fill="var(--label-bg)"/>
      </svg>
      <span>From</span>
      <span class="signoff__brand">Harvest Crown TV</span>
      <span>Family</span>
    </p>
  </section>
</body>
</html>
```